Medical marijuana farm

I need a professional looking letterhead for my incorporated company

TERRA-BLOOM Inc.

"Copper Ridge Farm"

I want the name "Terra bloom" done in a lime green colour, with a black background.... Also- instead of a hyphen I would like a creative "+" sign....

4817 alder street, Nova Scotia is the civic address

902-555-0183

```html
<!DOCTYPE html>
<html lang="en">
<head>
<meta charset="utf-8">
<title>Terra Bloom Inc. Letterhead</title>
<link rel="stylesheet" href="https://fonts.googleapis.com/css2?family=Cinzel:wght@500&family=Aladin&family=Niconne&display=swap">
<style>
  :root {
    --paper: #ffffff;
    --banner: #000000;
    --lime: #22d400;
    --ink: #1c1c1c;
  }
  html, body {
    margin: 0;
    padding: 0;
    overflow: hidden;
  }
  .letterhead {
    position: relative;
    width: 1000px;
    height: 1200px;
    background: var(--paper);
    overflow: hidden;
  }
  .banner {
    position: absolute;
    left: 70px;
    top: 10px;
    width: 844px;
    height: 203px;
    background: var(--banner);
  }
  .company-name {
    position: absolute;
    left: 0;
    right: 0;
    top: 52px;
    display: flex;
    justify-content: center;
    align-items: baseline;
    gap: 22px;
    font-family: "Cinzel", serif;
    font-weight: 500;
    color: var(--lime);
    font-size: 66px;
    line-height: 1;
    letter-spacing: 2px;
  }
  .company-name .mark {
    width: 40px;
    height: 40px;
    background: var(--lime);
    align-self: center;
  }
  .company-name .suffix {
    font-size: 30px;
    margin-left: -12px;
  }
  .farm-name {
    position: absolute;
    left: 205px;
    top: 150px;
    font-family: "Aladin", cursive;
    font-size: 38px;
    color: var(--lime);
    letter-spacing: 1px;
    margin: 0;
  }
  .address {
    position: absolute;
    left: 0;
    width: 964px;
    top: 1120px;
    text-align: center;
    font-family: "Niconne", cursive;
    font-size: 38px;
    color: var(--ink);
    margin: 0;
  }
</style>
</head>
<body>
  <div class="letterhead">
    <header class="banner">
      <h1 class="company-name">
        <span>TERRA</span>
        <span class="mark" aria-hidden="true"></span>
        <span>BLOOM.</span>
        <span class="suffix">INC</span>
      </h1>
      <p class="farm-name">Copper Ridge Farm</p>
    </header>
    <footer>
      <p class="address">4817 alder street, Nova Scotia</p>
    </footer>
  </div>
</body>
</html>
```